AMAZING BLACK FRIDAY AD FOR PRINT OR THE WEB

Create a Black Friday ad for nitrile gloves. We are offering a box of 100, no-powder, exam grade nitrile gloves, for $9.99. No limit. Each case is $99. Create something simple, eye catching, cool. BrisaVeil.com. Sale ends on December 4th. While supplies last. We are a local medical supply company in Hawaii that serves the general public in addition to local businesses, government, etc. Gloves are in short supply and we have tons of inventory ready to sell.

Target Market(s)

Businesses that use supplies such as gloves

Industry/Entity Type

medical supplies

Requirements
Must have
• logo and website

```html
<!DOCTYPE html>
<html lang="en">
<head>
<meta charset="utf-8">
<title>Black Friday Sale – Nitrile Gloves – BrisaVeil.com</title>
<link rel="stylesheet" href="https://fonts.googleapis.com/css2?family=League+Spartan:wght@500;600;700;800;900&family=Kaushan+Script&family=Open+Sans:wght@400;600&display=swap">
<style>
  :root {
    --ink: #141414;
    --ink-soft: #2e2e2e;
    --white: #ffffff;
    --paper: #f4f4f6;
    --green: #0fa84a;
    --red: #f11a1a;
    --rule: #4a4a4a;
    --price-frame: #8a7636;
    --glove-blue: #2fa8e8;
    --glove-deep: #1670b8;
    --body-text: #3a3a3a;
  }
  * { box-sizing: border-box; margin: 0; padding: 0; }
  html, body { width: 956px; height: 1200px; overflow: hidden; background: var(--ink); }
  .flyer {
    position: relative; width: 956px; height: 1200px; overflow: hidden;
    background: radial-gradient(circle at 80% 30%, #3c3c3c 0%, #222 35%, var(--ink) 70%);
    font-family: "League Spartan", "Montserrat", sans-serif;
    color: var(--white);
  }
  .deadline { position: absolute; left: 690px; top: 50px; line-height: 1; }
  .deadline__label { font-size: 24px; font-weight: 700; letter-spacing: 1px; }
  .deadline__date { font-size: 24px; font-weight: 700; color: var(--green); letter-spacing: 1px; margin-top: 2px; }
  .deadline__note { font-family: "Open Sans", sans-serif; font-size: 11px; margin-top: 4px; }

  .product-photo {
    position: absolute; left: 470px; top: 130px; width: 486px; height: 780px;
    background:
      radial-gradient(ellipse 45% 40% at 55% 40%, var(--glove-blue) 0%, var(--glove-deep) 55%, transparent 75%),
      radial-gradient(ellipse 55% 35% at 70% 78%, #0c0c0c 0%, #1a1a1a 60%, transparent 80%);
  }

  .headline { position: absolute; left: 60px; top: 40px; font-weight: 600; font-size: 156px; line-height: 0.82; letter-spacing: -2px; }
  .headline span { display: block; }
  .headline__script {
    position: absolute; left: 100px; top: 248px;
    font-family: "Kaushan Script", cursive; font-size: 118px; color: var(--red);
    transform: rotate(-8deg); line-height: 1;
  }
  .offer { position: absolute; left: 62px; top: 406px; }
  .offer__intro { font-size: 36px; font-weight: 700; color: var(--green); letter-spacing: 1.5px; line-height: 1; }
  .offer__qty { font-size: 54px; font-weight: 700; letter-spacing: 3px; line-height: 1; margin-top: 6px; }
  .product-name { position: absolute; left: 58px; top: 510px; font-size: 128px; font-weight: 900; color: var(--green); line-height: 0.8; letter-spacing: -1px; }

  .rule { position: absolute; left: 60px; width: 466px; height: 1px; background: var(--rule); }
  .rule--top { top: 714px; }
  .rule--bottom { top: 812px; }

  .features { position: absolute; left: 68px; top: 731px; display: flex; gap: 28px; align-items: center; }
  .feature { display: flex; align-items: center; gap: 14px; font-family: "Open Sans", sans-serif; font-size: 24px; line-height: 1.05; }
  .feature__icon { width: 56px; height: 56px; flex: none; }

  .pricing { position: absolute; left: 68px; top: 832px; display: flex; align-items: center; }
  .price-tag {
    border: 1.5px solid var(--price-frame); border-radius: 6px;
    padding: 6px 12px 0; font-size: 70px; font-weight: 800; line-height: 1; letter-spacing: 1px;
  }
  .price-tag sup { font-size: 34px; vertical-align: 30px; margin-right: 2px; }
  .price-note { font-size: 34px; font-weight: 700; color: var(--green); line-height: 0.9; letter-spacing: 1px; }
  .price-note--limit { margin: 0 42px 0 16px; }
  .price-note--case { margin-right: 10px; font-size: 44px; line-height: 0.8; }
  .price-note--case small { font-size: 34px; display: block; }

  .footer-tear { position: absolute; left: 0; top: 960px; width: 956px; height: 240px; }
  .about {
    position: absolute; left: 92px; top: 1052px; width: 470px;
    font-family: "Open Sans", sans-serif; font-size: 16.5px; line-height: 1.35; color: var(--body-text);
  }
  .brand { position: absolute; left: 655px; top: 1090px; display: flex; align-items: center; gap: 10px; }
  .brand__dot { width: 20px; height: 20px; border-radius: 50%; background: var(--green); }
  .brand__name { font-size: 40px; font-weight: 700; color: var(--green); letter-spacing: -0.5px; }
</style>
</head>
<body>
<main class="flyer">
  <div class="product-photo" role="img" aria-label="Photo of blue nitrile exam gloves rising out of a black plastic basket"></div>

  <div class="deadline">
    <div class="deadline__label">SALE ENDS ON</div>
    <div class="deadline__date">4TH DECEMBER</div>
    <div class="deadline__note">TILL SUPLIES LAST</div>
  </div>

  <h1 class="headline"><span>BLACK</span><span>FRIDAY</span></h1>
  <div class="headline__script">Sale</div>

  <div class="offer">
    <p class="offer__intro">WE ARE OFFERING</p>
    <p class="offer__qty">A BOX OF 100</p>
  </div>
  <h2 class="product-name">NITRILE<br>GLOVES</h2>

  <div class="rule rule--top"></div>
  <div class="features">
    <div class="feature">
      <svg class="feature__icon" viewBox="0 0 56 56" aria-hidden="true">
        <circle cx="28" cy="28" r="26" fill="none" stroke="var(--green)" stroke-width="2.5"/>
        <circle cx="28" cy="28" r="20" fill="var(--green)"/>
        <rect x="22" y="18" width="12" height="18" rx="2" fill="var(--ink)" transform="rotate(35 28 28)"/>
        <line x1="16" y1="16" x2="40" y2="40" stroke="var(--white)" stroke-width="2.5"/>
      </svg>
      <span>No-powder</span>
    </div>
    <div class="feature">
      <svg class="feature__icon" viewBox="0 0 56 56" aria-hidden="true">
        <circle cx="28" cy="28" r="26" fill="none" stroke="var(--green)" stroke-width="2.5"/>
        <circle cx="28" cy="28" r="20" fill="var(--green)"/>
        <path d="M20 16h11l6 6v18H20z" fill="none" stroke="var(--ink)" stroke-width="2.2"/>
        <text x="28" y="35" font-size="9" font-weight="700" text-anchor="middle" fill="var(--ink)" font-family="League Spartan, sans-serif">A+</text>
      </svg>
      <span>Exam grade<br>nitrile gloves</span>
    </div>
  </div>
  <div class="rule rule--bottom"></div>

  <div class="pricing">
    <div class="price-tag"><sup>$</sup>9.99</div>
    <div class="price-note price-note--limit">NO<br>LIMIT</div>
    <div class="price-note price-note--case">EACH<small>CASE IS</small></div>
    <div class="price-tag"><sup>$</sup>99</div>
  </div>

  <svg class="footer-tear" viewBox="0 0 956 240" preserveAspectRatio="none" aria-hidden="true">
    <path d="M0 62 L30 52 L52 58 L78 46 L110 50 L150 34 L190 38 L230 26 L270 30 L300 18 L330 22 L352 8 L380 14 L420 6 L470 10 L520 4 L560 8 L600 6 L640 12 L690 14 L740 24 L790 40 L830 52 L870 58 L910 70 L956 62 L956 240 L0 240 Z" fill="var(--paper)"/>
  </svg>

  <p class="about">We are a local medical supply company in Hawaii that serves the general public in addtion to local business, government, etc. Gloves are in short supply and we have tons of inventory ready to sell.</p>

  <div class="brand">
    <span class="brand__dot"></span>
    <span class="brand__name">BrisaVeil.com</span>
  </div>
</main>
</body>
</html>
```